Need a one sheet capability statement for my consulting company

We need a slick capability statement for an Aviation Consulting company. We provide Air Traffic Control, Aerospace Services and Enterprise IT Support for the Aviation community. Our customers are ORVEL, Airlines, Airports, and the Coastal Flight Directorate. We would to have a design that uses the scheme in our logo, and look a bit slick and very professional and impressive. The final design should clearly community that we are Aviation Experts.

Target Market(s)

Airlines, Coastal Flight Directorate, ORVEL, Air Traffic Control, Airports

Industry/Entity Type

Aviation

Colors
86cae7
33a6d7
85cae6

Requirements
Must have
• Nice colors that blend in well with our Logo. Easy to read capability document. Elegant and communicate professionalism
Nice to have
• Slick colors preferably sky blue, but open to whatever color the designers thinks will look great.

```html
<!DOCTYPE html>
<html lang="en">
<head>
<meta charset="utf-8">
<title>Corvane Consulting Group – Capability Statement</title>
<link href="https://fonts.googleapis.com/css2?family=Source+Sans+3:wght@400;600;700&family=Montserrat:wght@300;700&display=swap" rel="stylesheet">
<style>
:root{
  --bg:#e4e5e8;
  --navy:#2f3a6a;
  --navy-deep:#283460;
  --slate:#4a5e92;
  --slate-light:#5c71a6;
  --band:#283262;
  --orange:#f08a24;
  --text:#ffffff;
  --muted:#b9c6e6;
  --photo-sky:#9fb3cf;
  --photo-warm:#c79a6b;
}
*{box-sizing:border-box;margin:0;padding:0}
html,body{width:1200px;height:1200px;overflow:hidden;background:var(--bg)}
body{position:relative;font-family:"Source Sans 3",Arial,sans-serif;color:var(--text)}
.sheet{position:absolute;width:516px;height:668px;overflow:hidden;background:linear-gradient(180deg,var(--navy) 0%,var(--slate) 55%,var(--slate-light) 100%)}
.sheet--front{left:62px;top:90px}
.sheet--back{left:638px;top:424px}
.sheet svg.backdrop{position:absolute;inset:0}
.abs{position:absolute}
.url{font-size:8px;font-weight:700;font-style:italic}
.brand{font-weight:700;font-size:27px;letter-spacing:1px;line-height:1;color:#fff;display:flex;align-items:center;gap:6px}
.brand .dot{width:9px;height:9px;border-radius:50%;background:var(--orange)}
.brand-sub{font-size:5px;font-weight:600;letter-spacing:.4px;text-align:right}
.title{font-family:"Montserrat",Arial,sans-serif;line-height:.95;color:#fff}
.title .thin{font-weight:300;font-size:24px;display:block}
.title .bold{font-weight:700;font-size:24px;display:block}
.bar{position:absolute;height:13px;padding:0 10px;font-size:8.5px;font-weight:700;line-height:13px;color:#fff;background:var(--navy-deep);clip-path:polygon(0 0,100% 0,calc(100% - 12px) 100%,0 100%)}
.bar--orange{background:var(--orange)}
.bar--lg{height:17px;line-height:17px;font-size:10px}
.rule{position:absolute;height:1px;background:rgba(255,255,255,.35)}
.rule--orange{background:var(--orange)}
.info{font-size:8.3px;line-height:1.45}
.info b{font-weight:700}
.cert{font-size:10px;font-weight:700;color:var(--orange)}
.codes{display:grid;grid-template-columns:45px 45px 45px;font-size:8.3px;line-height:1.45}
.sub{font-size:8.5px;font-weight:600;color:var(--orange)}
.dots{list-style:none;font-size:8.3px;line-height:1.45}
.dots li::before{content:"";display:inline-block;width:3px;height:3px;background:var(--orange);margin:0 4px 1px 0;vertical-align:middle}
.arrows{list-style:none;font-size:8.2px;line-height:1.4}
.arrows li::before{content:"➢ ";font-size:7px}
.vehicles{position:absolute;left:46px;top:280px;display:flex;align-items:center;gap:8px}
.vehicle{width:82px;height:32px;border-radius:3px;background:linear-gradient(180deg,#3a4a80,#2b3766);box-shadow:2px 2px 3px rgba(0,0,0,.35);font-size:8.8px;text-align:center;line-height:1.3;padding-top:3px}
.vehicle b{font-weight:700;display:block}
.chev{width:8px;height:14px}
.refs{position:absolute;left:46px;top:370px;display:flex}
.ref{width:150px;padding-right:8px;font-size:7.2px;line-height:1.4;color:var(--muted)}
.ref + .ref{border-left:1px solid rgba(255,255,255,.3);padding-left:20px}
.ref .avatar{width:46px;height:46px;border-radius:50%;background:var(--navy-deep);margin:0 0 18px 18px;border:3px solid #dfe6f5}
.ref .name{font-size:8.8px;font-weight:700;color:#fff}
.ref .mail{color:#fff}
.band{position:absolute;left:0;right:0;top:504px;bottom:0;background:var(--band)}
</style>
</head>
<body>

<section class="sheet sheet--front">
  <svg class="backdrop" width="516" height="668" viewBox="0 0 516 668">
    <defs>
      <linearGradient id="launchTone" x1="0" y1="0" x2="0" y2="1">
        <stop offset="0" stop-color="var(--photo-sky)"/>
        <stop offset=".65" stop-color="var(--photo-warm)"/>
        <stop offset="1" stop-color="#6d6a6a"/>
      </linearGradient>
    </defs>
    <path d="M0 0 H330 C420 60 470 140 516 120 V0 Z" fill="var(--navy)"/>
    <path role="img" aria-label="Photograph of a rocket launching from its pad with clouds of exhaust" d="M0 70 C120 40 240 90 300 130 C360 180 300 300 170 320 C110 330 50 320 0 330 Z" fill="url(#launchTone)"/>
    <path d="M0 330 C170 310 380 260 460 190 C490 160 510 130 516 120 V170 C470 300 250 360 0 352 Z" fill="var(--slate)" opacity=".85"/>
    <path d="M330 0 C430 60 500 110 516 120" stroke="#8ea4d2" stroke-width="1.5" fill="none" opacity=".7"/>
  </svg>

  <div class="abs url" style="right:14px;top:18px">corvaneconsulting.com</div>
  <div class="abs" style="left:30px;top:38px">
    <div class="brand">CORVANE<span class="dot"></span></div>
    <div class="brand-sub">CONSULTING GROUP</div>
  </div>
  <h1 class="abs title" style="left:274px;top:106px"><span class="thin">COMMERCIAL</span><span class="bold">SPACE</span><span class="bold">INTEGRATION</span></h1>

  <div class="abs cert" style="left:315px;top:332px">MBE/DBE/SBE Certified</div>

  <div class="bar" style="left:24px;top:353px;width:244px">Corporate Information</div>
  <div class="abs info" style="left:34px;top:370px;width:240px">
    <b style="font-size:8.8px">President: Daniel R. Marchetti</b><br>
    <b>T</b> : (202) 555-0143 | <b>E</b> : daniel.marchetti@corvaneconsulting.com<br>
    <b>W</b> : www.corvaneconsulting.com
    <p style="margin-top:9px;width:220px"><b>Certifications</b> : Agile Scrumaster, Lean Six Sigma Greenbelt, SVQL, DARF, PMNX, FRAX, DocuHub, CSSX, Tabrix, QuarryDB</p>
    <p style="margin-top:9px"><b>Tools</b> : VECTRA, Model Forge, KESTA, DocuHub</p>
  </div>

  <div class="bar" style="left:306px;top:353px;width:176px">Primary NAICs Codes</div>
  <div class="abs info" style="left:315px;top:370px">
    <div class="codes"><span>541511</span><span>541611</span><span>488111</span><span>541512</span><span>541330</span><span>561110</span></div>
    <b>PSC Codes</b><br>R408R425U008 U009<br>D302 D307D308 D310 D314
    <p style="margin-top:9px">D-U-N-S: 061537204 Cage Code: 4KQ8M</p>
  </div>

  <div class="rule" style="left:24px;right:28px;top:482px"></div>
  <div class="bar bar--orange" style="left:24px;top:482px;width:104px">Company Overview</div>
  <p class="abs info" style="left:34px;top:500px;width:455px;line-height:1.65">Corvane Consulting Group, Inc. is a minority owned small business that provides strategic planning, and technology integration solutions for the Aviation and Aerospace community. Our strategic planning and technology expertise lies in the areas of Air Traffic Management, UAS Rules and Regulations, Cloud Migration, Cybersecurity, and Enterprise Architecture.</p>

  <div class="rule" style="left:24px;right:28px;top:560px"></div>
  <div class="bar" style="left:24px;top:560px;width:104px;font-size:9px">Service Offerings</div>
  <div class="abs" style="left:34px;top:576px">
    <div class="sub">Information Technology Services</div>
    <ul class="dots" style="margin-top:3px"><li>Enterprise Architecture</li><li>Systems Engineering</li><li>Business Process Engineering</li><li>Software Engineering</li><li>Cloud Computing/Migration</li></ul>
  </div>
  <div class="abs" style="left:260px;top:576px">
    <div class="sub">Aviation Services</div>
    <ul class="dots" style="margin-top:3px"><li>Air Traffic Program Management</li><li>Air Traffic Staffing Support i.e ZHB, ZKT, ZRM, ZWL</li><li>UAS Policy and Procedures</li><li>Commercial Space Transporation</li><li>Safety and Feasiblity Studies</li></ul>
  </div>
</section>

<section class="sheet sheet--back">
  <svg class="backdrop" width="516" height="668" viewBox="0 0 516 668">
    <path d="M0 0 H516 V110 C440 30 300 0 0 0 Z" fill="var(--slate)" opacity=".6"/>
    <path d="M200 0 C350 20 480 80 516 120" stroke="#8ea4d2" stroke-width="1.2" fill="none" opacity=".6"/>
    <path d="M0 300 C120 230 300 140 516 130 V504 H0 Z" fill="var(--slate-light)" opacity=".35"/>
  </svg>

  <div class="abs" style="right:36px;top:36px">
    <div class="brand" style="font-size:24px">CORVANE<span class="dot"></span></div>
    <div class="brand-sub">CONSULTING GROUP</div>
  </div>

  <div class="bar bar--lg" style="left:38px;top:40px;width:180px">Notable CFD Past Performances</div>
  <ul class="abs arrows" style="left:46px;top:60px">
    <li>Harbor Corridor Route Program Management Support (HCRP) - Airspace Services</li>
    <li>UAS Flight Authorization (UFA), and Records Request Approvals - Office of Emerging Technology</li>
    <li>Airspace Enterprise Architecture - Joint Airspace Planning Office (JAPO)</li>
    <li>DocuHub Management &amp; Maitenance</li>
  </ul>

  <div class="rule rule--orange" style="left:38px;right:0;top:117px"></div>
  <div class="bar bar--orange bar--lg" style="left:38px;top:117px;width:112px">Why Hire us?</div>
  <ul class="abs arrows" style="left:46px;top:139px">
    <li>Expert team of retired controllers with over 20 years of Air Traffic Control and Center Management experience</li>
    <li>Systems engineers with strong knowledge of ALM Processes</li>
    <li>Experts in Cyber Security Policies and FSCA Compliance</li>
    <li>Experts in Enteprise Architecture frameworks such as DARF and FRAX</li>
    <li>Experience performing UAS Integration feasibility studies and technology evaluation</li>
    <li>National Transportation Research Fellows</li>
    <li>Competitive pricing and cost effective rates</li>
  </ul>

  <div class="rule rule--orange" style="left:38px;right:0;top:240px"></div>
  <div class="bar bar--orange bar--lg" style="left:38px;top:240px;width:112px">How to get to us?</div>
  <div class="vehicles">
    <div class="vehicle"><b>Supply Schedule 41</b>(Prime)</div>
    <svg class="chev" viewBox="0 0 8 14"><path d="M1 1 L7 7 L1 13" stroke="#2b3766" stroke-width="2" fill="none"/></svg>
    <div class="vehicle"><b>CFD eVANT</b>(Prime)</div>
    <svg class="chev" viewBox="0 0 8 14"><path d="M1 1 L7 7 L1 13" stroke="#2b3766" stroke-width="2" fill="none"/></svg>
    <div class="vehicle"><b>eCORE</b>(SubContractor)</div>
    <svg class="chev" viewBox="0 0 8 14"><path d="M1 1 L7 7 L1 13" stroke="#2b3766" stroke-width="2" fill="none"/></svg>
    <div class="vehicle"><b>Sv2030</b>(Subcontractor)</div>
  </div>

  <div class="rule rule--orange" style="left:38px;right:0;top:335px"></div>
  <div class="bar bar--orange bar--lg" style="left:38px;top:335px;width:148px">Professional References</div>
  <div class="refs">
    <div class="ref">
      <div class="avatar" role="img" aria-label="Portrait icon of the reference"></div>
      <div class="name">Mr. Martin Halvorsen</div>Coastal Flight Directorate,<br>Director- Mission Support Services<br><span class="mail">Martin.halvorsen@cfd.gov</span>
    </div>
    <div class="ref" style="width:140px">
      <div class="avatar" role="img" aria-label="Portrait icon of the reference"></div>
      <div class="name">Mr. Alden Whitaker</div>Coastal Flight Directorate<br>Manager- Airspace Services<br><span class="mail">Alden.Whitaker@cfd.gov</span>
    </div>
    <div class="ref" style="width:170px">
      <div class="avatar" role="img" aria-label="Portrait icon of the reference"></div>
      <div class="name">Mr. Reid Walcott</div>Coastal Flight Directorate<br>Manager- Maintenance Automation Team<br><span class="mail">Reid.walcott@cfd.gov</span>
    </div>
  </div>

  <div class="band">
    <div class="rule" style="left:38px;right:0;top:24px"></div>
    <div class="bar bar--lg" style="left:38px;top:24px;width:190px;background:#3a4a80">Our White Papers Publications</div>
    <ul class="abs arrows" style="left:46px;top:52px;line-height:1.75">
      <li>Drones for Aid- A Study on effective use of Unmanned Aerial Systems during Disaster Relief</li>
      <li>SGMS-X, an alternative study of how to prevent runway incursion</li>
      <li>Drones Infra-Red Camera Technology- A study on how to use drones to facilitate crop dusting</li>
      <li>Cloud Computing- An acquisition strategy guide</li>
      <li>Cloud Migration Approach Best Practices</li>
      <li>Database Replication Pros and Cons</li>
    </ul>
    <div class="abs url" style="right:36px;top:138px;color:var(--orange)">corvaneconsulting.com</div>
  </div>
</section>

</body>
</html>
```